Tidewell Homecare

I am looking to have a website designed for a housekeeping company that looks similar to this one. https://marlowsnestcare.example/

I need 5 websites designed but will start with this one to see how I like it.

Industry/Entity Type

House Cleaning

Coding

Coded - Design and coding required

Number of Pages Required

5+ page

Font styles to use
Serif
Script

Colors
ffffff
fdf9cf
fbf289
fbee3f
d6edf3
86cae7
33a6d7
edf1f8
cedeed

```html
<!DOCTYPE html>
<html lang="en">
<head>
<meta charset="utf-8">
<title>Tidewell Homecare</title>
<link href="https://fonts.googleapis.com/css2?family=Open+Sans:ital,wght@0,400;0,600;0,700;1,400&family=Playfair+Display:wght@400;700&display=swap" rel="stylesheet">
<style>
:root{
  --ink:#333;
  --muted:#555;
  --topbar:#efefef;
  --accent:#2f9fb8;
  --nav-active:#2a7fd4;
  --green:#5cc86a;
  --green-dark:#4bb75a;
  --sky:#62b0d4;
  --form-bg:#efefef;
  --form-line:#d5d5d5;
  --legend:#9b1c1c;
  --submit:#4d6c97;
  --mint:#d9fcd9;
  --footer:#2e3d5c;
  --footer-base:#243150;
  --white:#fff;
}
*{box-sizing:border-box;margin:0;padding:0}
html,body{width:1200px;height:3850px;overflow:hidden;background:var(--white)}
body{font-family:"Open Sans",Arial,sans-serif;color:var(--ink)}
.serif{font-family:"Playfair Display",Georgia,serif}

.topbar{height:36px;background:var(--topbar);display:flex;align-items:center;justify-content:center;font-size:15px;color:#444}
.topbar strong{margin-left:4px;color:#222}

.site-nav{height:94px;display:flex;align-items:center;justify-content:space-between;padding:0 95px}
.brand{display:flex;align-items:center;gap:10px;font-family:"Open Sans",sans-serif;font-weight:600;font-size:17px;color:var(--accent)}
.brand-dot{width:22px;height:22px;border-radius:50%;background:var(--accent)}
.menu{display:flex;gap:19px;list-style:none;font-size:15.5px}
.menu li{color:#444}
.menu li.active{color:var(--nav-active)}

.hero{position:relative;height:722px;background:linear-gradient(160deg,#c8b998 0%,#e9e4d7 35%,#d9cfbd 60%,#8a6a45 100%)}
.hero-panel{position:absolute;left:69px;right:69px;top:200px;height:384px;background:rgba(255,255,255,.86);text-align:center;padding:0 50px}
.hero-badge{position:absolute;left:50%;top:-62px;transform:translateX(-50%);width:140px;height:140px;border-radius:50%;background:var(--white);display:flex;align-items:center;justify-content:center;font-weight:600;font-size:15px;color:var(--accent);box-shadow:0 2px 8px rgba(0,0,0,.08)}
.hero h1{font-family:"Playfair Display",serif;font-weight:400;font-size:27px;color:#333;margin-top:98px;letter-spacing:.3px}
.hero p{font-size:15px;line-height:25.5px;color:#444;margin-top:14px}
.hero .chev{margin-top:26px}

.services{height:459px;display:flex;padding:60px 20px 0 80px}
.service{flex:1;text-align:center;padding:0 8px}
.service-icon{height:94px;display:flex;justify-content:center;align-items:flex-end}
.service h2{font-family:"Playfair Display",serif;font-weight:400;font-size:23px;margin-top:28px;color:#333}
.service p{font-size:15px;line-height:25.5px;color:#555;margin-top:18px}
.btn-green{display:inline-block;margin-top:18px;background:var(--green);color:var(--white);font-size:13.5px;padding:9px 23px;text-transform:uppercase;border-bottom:2px solid var(--green-dark)}

.about-band{height:395px;display:flex}
.about-photo{width:600px;background:linear-gradient(180deg,#9fb0c6 0%,#dde4ec 35%,#4b5a4c 60%,#e9ecef 100%)}
.about-copy{flex:1;background:var(--sky);color:var(--white);padding:44px 48px 0 48px}
.about-copy h2{font-family:"Playfair Display",serif;font-weight:400;font-size:27px}
.about-copy p{font-size:15px;line-height:25.5px;margin-top:16px;color:#eef6fb}
.btn-outline{display:inline-block;margin-top:30px;background:var(--white);color:var(--sky);font-size:13.5px;padding:8px 22px;text-transform:uppercase}

.estimate{height:917px;padding-top:62px}
.estimate h2{font-family:"Playfair Display",serif;font-weight:400;font-size:27px;text-align:center;color:#333}
.form-box{width:824px;margin:34px auto 0;background:var(--form-bg);border:1px solid var(--form-line);padding:10px 20px 20px}
.form-box + .form-box{margin-top:15px}
.legend{font-family:"Playfair Display",serif;font-size:19px;color:var(--legend);border-bottom:1px solid #ccc;padding:4px 0 6px}
.grid{display:grid;grid-template-columns:1fr 1fr;column-gap:64px}
.field{margin-top:13px}
.field.full{grid-column:1/3}
.field label{display:block;font-size:11.5px;font-weight:700;color:#222;margin-bottom:6px}
.field label i{color:#c00;font-style:normal}
.input{height:36px;background:var(--white);border:1px solid #ccc;border-radius:3px;font-size:12px;color:#444;padding:0 13px;display:flex;align-items:center;justify-content:space-between}
.input .arrow{width:14px;height:36px;border-left:1px solid #999;margin-right:-13px;display:flex;align-items:center;justify-content:center}
.short{width:390px}
.hint{font-size:11px;color:#444;margin-top:10px}
.submit{display:inline-block;margin-top:14px;background:var(--submit);color:var(--white);font-size:12px;font-weight:700;padding:9px 12px;border-radius:2px}
.request{height:484px}
.verify{height:202px}

.vendors{height:366px;background:var(--mint);padding-top:52px}
.vendors h2{font-family:"Playfair Display",serif;font-weight:400;font-size:27px;text-align:center;color:#333}
.vendor-row{display:flex;gap:19px;justify-content:center;margin-top:26px}
.vendor{width:336px;height:187px;display:flex;align-items:center;justify-content:center;color:var(--white);font-size:19px;font-weight:600}
.v1{background:linear-gradient(135deg,#3c3c3c,#1f1f1f)}
.v2{background:linear-gradient(135deg,#5a4a3a,#2c2720)}
.v3{background:linear-gradient(135deg,#4d4945,#35322f)}

.testimonial{position:relative;height:472px;background:linear-gradient(120deg,#2d7ed0 0%,#3a90dc 55%,#5ea6d8 85%,#c8d24a 100%)}
.quote{position:absolute;left:122px;right:124px;top:86px;height:186px;background:rgba(236,240,246,.92);text-align:center;padding:20px 22px;font-style:italic;font-size:21px;line-height:29.5px;color:#555}
.quote:after{content:"";position:absolute;bottom:-14px;left:50%;margin-left:-14px;border:14px solid transparent;border-bottom:0;border-top-color:rgba(236,240,246,.92)}
.author{position:absolute;top:290px;left:0;right:0;display:flex;justify-content:center;align-items:center;gap:14px;color:var(--white);font-size:13px;font-weight:700}
.avatar{width:48px;height:48px;border-radius:50%;background:#e6eef6}
.dots{position:absolute;top:390px;left:0;right:0;display:flex;justify-content:center;gap:12px}
.dots span{width:4px;height:4px;border-radius:50%;background:rgba(255,255,255,.5)}
.dots span.on{background:#1c2a44}
.slide-arrow{position:absolute;top:215px}

.site-footer{height:317px;background:var(--footer);display:flex;padding:62px 110px 0;color:var(--white)}
.foot-col{width:342px}
.foot-col h3{font-size:18.5px;font-weight:600}
.foot-col p,.foot-col li{font-size:15px;line-height:25px;color:#e4e8f0}
.foot-col ul{list-style:none;margin-top:10px}
.foot-col .stack{margin-top:10px}
.signup{display:flex;margin-top:20px}
.signup .email{width:194px;height:36px;background:#eef1f5;border:1px solid #ccc;font-size:12px;color:#888;display:flex;align-items:center;padding-left:12px}
.signup .go{margin-left:4px;height:36px;background:#4d6c97;font-size:11.5px;font-weight:700;display:flex;align-items:center;padding:0 12px;text-transform:uppercase}
.copyright{height:72px;background:var(--footer-base);display:flex;align-items:center;justify-content:center;color:#e4e8f0;font-size:15px}
</style>
</head>
<body>

<div class="topbar">Contact us for more information: <strong>555-204-7781</strong></div>

<header class="site-nav">
  <div class="brand"><span class="brand-dot"></span>Tidewell Homecare</div>
  <ul class="menu">
    <li class="active">Home</li><li>Services</li><li>About</li><li>Testimonials</li><li>Contact</li><li>Free Estimate</li>
  </ul>
</header>

<section class="hero" role="img" aria-label="Bright, tidy living room with white sofa, hardwood floor and chandelier">
  <div class="hero-panel">
    <div class="hero-badge">Tidewell Homecare</div>
    <h1>THE IMPORTANCE OF GOOD HOUSEKEEPING</h1>
    <p>Lorem ipsum dolor sit amet, consectetur adipiscing elit, sed do eiusmod tempor incididunt ut labore et dolore magna aliqua. Ut enim ad minim veniam, quis nostrud exercitation ullamco laboris nisi ut aliquip ex ea commodo consequat. Duis aute irure dolor in reprehenderit in voluptate velit esse cillum dolore eu fugiat nulla pariatur. Excepteur sint occaecat cupidatat non proident, sunt in culpa qui officia deserunt mollit anim id est laborum.</p>
    <svg class="chev" width="42" height="26" viewBox="0 0 42 26"><path d="M4 4 L21 21 L38 4" fill="none" stroke="#5cc86a" stroke-width="6" stroke-linecap="round" stroke-linejoin="round"/></svg>
  </div>
</section>

<section class="services">
  <div class="service">
    <div class="service-icon"><div role="img" aria-label="Illustration of a small house with a cleaning brush" style="width:80px;height:80px;background:linear-gradient(135deg,#7fd07f,#f0a64a);border-radius:6px"></div></div>
    <h2>Residental Cleaning</h2>
    <p>Duis aute irure dolor in reprehenderit in voluptate velit esse cillum dolore eu fugiat nulla pariatur. Excepteur sint occaecat cupidatat non proident, sunt in culpa qui officia deserunt mollit anim id est laborum.</p>
    <span class="btn-green">Residental Services</span>
  </div>
  <div class="service">
    <div class="service-icon"><div role="img" aria-label="Illustration of an office building with a broom" style="width:80px;height:96px;background:linear-gradient(135deg,#b07fd0,#7fd07f);border-radius:6px"></div></div>
    <h2>Commercial/Office Cleaning</h2>
    <p>Lorem ipsum dolor sit amet, consectetur adipiscing elit, sed do eiusmod tempor incididunt ut labore et dolore magna aliqua. Ut enim ad minim veniam, quis nostrud exercitation ullamco laboris nisi ut aliquip ex ea commodo consequat.</p>
    <span class="btn-green">Commercial Services</span>
  </div>
</section>

<section class="about-band">
  <div class="about-photo" role="img" aria-label="Cleaning team standing beside the company van in a snowy mountain valley"></div>
  <div class="about-copy">
    <h2>Hard Work &amp; Reliability</h2>
    <p>Lorem ipsum dolor sit amet, consectetur adipiscing elit, sed do eiusmod tempor incididunt ut labore et dolore magna aliqua. Ut enim ad minim veniam, quis nostrud exercitation ullamco laboris nisi ut aliquip ex ea commodo consequat. Duis aute irure dolor in reprehenderit in voluptate velit esse cillum dolore eu fugiat nulla pariatur. Excepteur sint occaecat cupidatat non proident, sunt in culpa qui officia deserunt mollit anim id est laborum.</p>
    <span class="btn-outline">Get to know us</span>
  </div>
</section>

<section class="estimate">
  <h2>Free Estimate / Contact Us</h2>
  <div class="form-box request">
    <div class="legend">Request</div>
    <div class="grid">
      <div class="field full"><label>Name <i>*</i></label><div class="input"></div></div>
      <div class="field"><label>Email</label><div class="input"></div></div>
      <div class="field"><label>City <i>*</i></label><div class="input"></div></div>
      <div class="field"><label>Square Footage <i>*</i></label><div class="input"></div></div>
      <div class="field"><label>Property Type <i>*</i></label><div class="input">House<span class="arrow"><svg width="6" height="4"><path d="M0 0h6L3 4z" fill="#222"/></svg></span></div></div>
      <div class="field"><label>Type of Cleaning <i>*</i></label><div class="input">Residential<span class="arrow"><svg width="6" height="4"><path d="M0 0h6L3 4z" fill="#222"/></svg></span></div></div>
      <div class="field"><label>Frequency <i>*</i></label><div class="input">Weekly<span class="arrow"><svg width="6" height="4"><path d="M0 0h6L3 4z" fill="#222"/></svg></span></div></div>
      <div class="field full"><label>Date <i>*</i></label><div class="input"></div></div>
    </div>
  </div>
  <div class="form-box verify">
    <div class="legend">Verification</div>
    <div class="field"><label>Please enter any two digits <i>*</i></label><div class="input short"></div></div>
    <div class="hint">Example: 12</div>
    <span class="submit">SUBMIT</span>
  </div>
</section>

<section class="vendors">
  <h2>Preferred Vendors</h2>
  <div class="vendor-row">
    <div class="vendor v1">The Linen Loft, llc</div>
    <div class="vendor v2">Ridgeview Rentals</div>
    <div class="vendor v3">Brightline Restoration</div>
  </div>
</section>

<section class="testimonial" role="img" aria-label="Close-up of colourful cleaning sponges and spray bottles on a blue surface">
  <svg class="slide-arrow" style="left:82px" width="12" height="20" viewBox="0 0 12 20"><path d="M10 2 L2 10 L10 18" fill="none" stroke="#fff" stroke-width="2.5"/></svg>
  <svg class="slide-arrow" style="right:80px" width="12" height="20" viewBox="0 0 12 20"><path d="M2 2 L10 10 L2 18" fill="none" stroke="rgba(255,255,255,.6)" stroke-width="2.5"/></svg>
  <div class="quote">Duis aute irure dolor in reprehenderit in voluptate velit esse cillum dolore eu fugiat nulla pariatur. Excepteur sint occaecat cupidatat non proident, sunt in culpa qui officia deserunt mollit anim id est laborum. Lorem ipsum dolor sit amet, consectetur adipiscing elit, sed do eiusmod tempor incididunt ut labore et dolore magna aliqua. Ut enim ad minim veniam, quis nostrud exercitation ullamco laboris nisi ut aliquip ex ea commodo consequat.</div>
  <div class="author"><span class="avatar"></span>Dana R.</div>
  <div class="dots"><span></span><span class="on"></span><span></span></div>
</section>

<footer class="site-footer">
  <div class="foot-col">
    <h3>Contact</h3>
    <div class="stack"><p>PO Box 118 | Alder Springs, co 80417</p><p>hello@tidewellhomecare.example</p></div>
    <p style="margin-top:20px">555-204-7781</p>
  </div>
  <div class="foot-col">
    <h3>Quick Access</h3>
    <ul><li>Home</li><li>Services</li><li>About</li><li>Testimonials</li><li>Contact</li><li>Free Estimate</li></ul>
  </div>
  <div class="foot-col">
    <h3>Signup To Our Newsletter</h3>
    <div class="signup"><span class="email">Enter Your Email address</span><span class="go">Subscribe</span></div>
  </div>
</footer>
<div class="copyright">© 2020 Housekeeping. All Rights Reserved.</div>

</body>
</html>
```